Brochure & Business card design

Looking for a new business card design i want it to be modern and sharp looking i usually order plastic business cards, and i would like to make the colors like the logo teal/charcoal i will like to have our services on icons with words.... our services are
ROOFING GUTTERS PAINTING PRESSURE WASHING EXTERIOR DESIGN & ATTIC VENTILATION. I also want to add my credentials

Target Market(s)

Oregon local market

Industry/Entity Type

Residential Construction

Contact Information for Business Card

Business info, services, number, website

Font styles to use
Serif
Sans Serif

Colors
33b8a4
5c5c5c
ffffff

Requirements
Must have
• Dale Finch
• Cell:
• Office:
• Email:
• Website:
• also i need our social media icons
• Services ROOFING GUTTERS PAINTING PRESSURE WASHING EXTERIOR DESIGN & ATTIC VENTILATION
• -icons for number, web, email, cell
• OR #584312
• Wa #KTRABLD461X7
Nice to have
• -Clean design Front & Back
• -Icons
• -shape House just like logo design
• -First Impression
Should not have
• Not Busy or lost of eye contact

```html
<!DOCTYPE html>
<html lang="en">
<head>
<meta charset="utf-8">
<title>Kestrel Exteriors — Business Card</title>
<link href="https://fonts.googleapis.com/css2?family=Arimo:wght@400;700&display=swap" rel="stylesheet">
<style>
  :root{
    --teal:#33b8a4;
    --charcoal:#5c5c5c;
    --charcoal-dark:#434343;
    --white:#ffffff;
    --backdrop:#2b2b2b;
  }
  *{margin:0;padding:0;box-sizing:border-box}
  html,body{width:1200px;height:997px;overflow:hidden;background:var(--backdrop)}
  .canvas{position:relative;width:1200px;height:997px}
  .card{position:absolute;left:280px;width:640px;height:366px;overflow:hidden;background:var(--white);
        box-shadow:0 10px 30px rgba(0,0,0,.45);font-family:"Arimo",Arial,sans-serif}
  .card--services{top:70px}
  .card--contact{top:540px}
  .card svg.card__art{position:absolute;inset:0;width:100%;height:100%}

  /* services side */
  .brand-line{position:absolute;left:40px;top:72px}
  .brand-line__name{font-weight:700;font-size:26px;color:var(--teal);letter-spacing:1px}
  .brand-line__tag{font-size:12px;color:var(--charcoal);letter-spacing:3px;margin-top:6px}
  .services{position:absolute;right:34px;top:120px;list-style:none;text-align:right}
  .services li{font-size:13px;color:var(--white);letter-spacing:.5px;line-height:18px}
  .services li::after{content:"";display:inline-block;width:6px;height:6px;border-radius:50%;background:var(--charcoal);margin-left:8px;vertical-align:middle}
  .brand-mark{position:absolute;left:40px;bottom:40px;font-weight:700;font-size:56px;color:var(--white);letter-spacing:3px}

  /* contact side */
  .brand-block{position:absolute;left:0;right:0;top:60px;text-align:center}
  .brand-block__name{display:inline-flex;align-items:center;gap:10px;font-weight:700;font-size:30px;color:var(--teal);letter-spacing:1px}
  .brand-block__dot{width:14px;height:14px;background:var(--charcoal)}
  .brand-block__tag{font-size:12px;color:var(--charcoal);letter-spacing:3px;margin-top:8px}
  .person{position:absolute;left:42px;top:222px}
  .person__name{font-weight:700;font-size:20px;color:var(--teal);letter-spacing:1px}
  .person__role{font-size:13px;color:var(--white);margin-top:2px}
  .contact-list{position:absolute;left:42px;top:272px;list-style:none}
  .contact-list li{display:flex;align-items:flex-start;gap:10px;font-size:13px;color:var(--white);line-height:17px;margin-bottom:5px}
  .contact-list svg{flex:none;width:16px;height:16px;margin-top:1px}
  .social{position:absolute;right:30px;top:172px;text-align:right}
  .social__icons{display:flex;gap:5px;justify-content:flex-end}
  .social__icons span{width:16px;height:16px;background:var(--teal)}
  .social__handle{font-size:14px;color:var(--white);margin-top:6px}
</style>
</head>
<body>
<main class="canvas">

  <section class="card card--services" aria-label="Card back with services">
    <svg class="card__art" viewBox="0 0 640 366" aria-hidden="true">
      <rect width="640" height="366" fill="#ffffff"/>
      <path d="M0 366 L0 250 C170 190 400 215 640 70 L640 366 Z" fill="var(--teal)"/>
      <path d="M160 238 C360 215 520 160 640 55 L640 70 C520 175 360 225 160 238 Z" fill="var(--charcoal)"/>
      <path d="M0 262 C90 236 150 226 200 224 C130 232 60 250 0 272 Z" fill="var(--charcoal)"/>
    </svg>
    <div class="brand-line">
      <div class="brand-line__name">KESTREL EXTERIORS</div>
      <div class="brand-line__tag">BUILT RIGHT, BUILT ONCE.</div>
    </div>
    <ul class="services">
      <li>ROOFING</li>
      <li>GUTTERS</li>
      <li>PAINTING</li>
      <li>EXTERIOR DESIGN</li>
      <li>ATTIC VENTILATION</li>
      <li>PRESSURE WASHING</li>
    </ul>
    <div class="brand-mark">KESTREL</div>
  </section>

  <section class="card card--contact" aria-label="Card front with contact details">
    <svg class="card__art" viewBox="0 0 640 366" aria-hidden="true">
      <rect width="640" height="366" fill="#ffffff"/>
      <path d="M0 366 L0 218 C200 158 430 170 640 112 L640 366 Z" fill="var(--charcoal-dark)"/>
      <path d="M0 204 C200 146 430 158 640 100 L640 114 C430 172 200 162 0 220 Z" fill="var(--teal)"/>
      <path d="M250 190 C420 196 540 170 640 128 L640 134 C540 180 420 204 250 190 Z" fill="var(--teal)"/>
    </svg>
    <div class="brand-block">
      <div class="brand-block__name"><span class="brand-block__dot"></span>KESTREL EXTERIORS</div>
      <div class="brand-block__tag">BUILT RIGHT, BUILT ONCE.</div>
    </div>
    <div class="social">
      <div class="social__icons"><span></span><span></span></div>
      <div class="social__handle">/kestrel-ext</div>
    </div>
    <div class="person">
      <div class="person__name">OWEN HARTLEY</div>
      <div class="person__role">General Manager</div>
    </div>
    <ul class="contact-list">
      <li><svg viewBox="0 0 16 16"><circle cx="8" cy="8" r="8" fill="#e6e6e6"/><path d="M5 4h2l1 2-1 1c.5 1 1 1.5 2 2l1-1 2 1v2c-4 0-7-3-7-7z" fill="var(--teal)"/></svg>0161 555 0182</li>
      <li><svg viewBox="0 0 16 16"><circle cx="8" cy="8" r="8" fill="#e6e6e6"/><rect x="4" y="5" width="8" height="6" fill="var(--teal)"/><path d="M4 5l4 3 4-3" stroke="#e6e6e6" fill="none"/></svg>ohartley@kestrel-ext.co.uk</li>
      <li><svg viewBox="0 0 16 16"><circle cx="8" cy="8" r="8" fill="#e6e6e6"/><path d="M8 3a3 3 0 0 1 3 3c0 2-3 6-3 6S5 8 5 6a3 3 0 0 1 3-3z" fill="var(--teal)"/></svg><span>Elm Row Dunmore<br>Fernbridge FB2 7QL</span></li>
    </ul>
  </section>

</main>
</body>
</html>
```